Business card design

I already have the logo design completed and am requiring business card design and layout utilising the logo. I require a front and back design.

We are an executive recruitment company so we are looking at full colour, high finish in a reasonably conservative structure.

Reason: will be provide ai template

Target Market(s)

Senior Management 35-60 age bracket

Industry/Entity Type

Business

Requirements
Must have
• Oliver Brantley
• Director
• 42 Morrow Tce, Ashgrove QLD 4060
• Ph: 07 3846 2190 Mob: 0418527396
• oliver@vantorapartners.com.au
• www.vantorapartners.com.au
Nice to have
• Ideally full colour,
Should not have
• cheap looking

```html
<!DOCTYPE html>
<html lang="en">
<head>
<meta charset="utf-8">
<title>Vantora Partners – Business Cards</title>
<link href="https://fonts.googleapis.com/css2?family=Roboto+Condensed:wght@400;500&display=swap" rel="stylesheet">
<style>
  :root {
    --backdrop: #e9e6e1;
    --card: #ffffff;
    --card-edge: #dcdcdc;
    --band: #f1f1f1;
    --brand-blue: #2f5f95;
    --link-blue: #3a6eaa;
    --ink-grey: #8a8d91;
    --ink-dark: #55595e;
    --mark-grey: #4a4f56;
  }
  * { margin: 0; padding: 0; box-sizing: border-box; }
  html, body {
    width: 1200px;
    height: 900px;
    overflow: hidden;
    background: var(--backdrop);
    font-family: "Roboto Condensed", "Arial Narrow", sans-serif;
  }
  .sheet {
    width: 1200px;
    height: 900px;
    display: flex;
    flex-direction: column;
    align-items: center;
    justify-content: center;
    gap: 40px;
  }
  .card {
    position: relative;
    width: 620px;
    height: 378px;
    background: var(--card);
    border: 1px solid var(--card-edge);
    box-shadow: 0 6px 18px rgba(0, 0, 0, 0.12);
  }
  .brand {
    display: flex;
    align-items: center;
    gap: 12px;
    color: var(--brand-blue);
    font-weight: 500;
    text-transform: uppercase;
    letter-spacing: 0.08em;
    white-space: nowrap;
  }
  .brand-square {
    background: var(--mark-grey);
    flex: none;
  }
  .web {
    color: var(--ink-grey);
    font-weight: 500;
    border-bottom: 2px solid var(--link-blue);
    white-space: nowrap;
  }
  .web-domain { color: var(--link-blue); }

  /* Back card */
  .card--back .brand {
    position: absolute;
    left: 40px;
    bottom: 40px;
    font-size: 20px;
  }
  .card--back .brand-square { width: 22px; height: 22px; }
  .card--back .web {
    position: absolute;
    right: 40px;
    bottom: 40px;
    font-size: 24px;
  }
  .contact {
    position: absolute;
    right: 40px;
    top: 70px;
    width: 330px;
    padding: 14px 16px;
    background: var(--band);
    text-align: right;
    font-size: 15px;
    line-height: 1.55;
    color: var(--ink-dark);
    font-style: normal;
  }
  .contact-label { color: var(--brand-blue); font-weight: 500; }

  /* Front card */
  .card--front {
    display: flex;
    flex-direction: column;
    align-items: center;
    justify-content: center;
    gap: 16px;
  }
  .card--front .brand { font-size: 38px; gap: 16px; }
  .card--front .brand-square { width: 40px; height: 40px; }
  .person {
    background: var(--band);
    padding: 6px 22px;
    text-align: center;
    color: var(--ink-dark);
    font-size: 18px;
    white-space: nowrap;
  }
  .person-name { font-weight: 500; color: var(--brand-blue); }
  .card--front .web { font-size: 28px; }
</style>
</head>
<body>
  <main class="sheet">
    <section class="card card--back" aria-label="Card back">
      <address class="contact">
        42 Morrow Tce, Ashgrove QLD 4060<br>
        <span class="contact-label">Ph:</span> 07 3846 2190 &nbsp; <span class="contact-label">Mob:</span> 0418527396<br>
        oliver@vantorapartners.com.au<br>
        www.vantorapartners.com.au
      </address>
      <div class="brand"><span class="brand-square"></span>Vantora Partners</div>
      <p class="web">vantorapartners<span class="web-domain">.com.au</span></p>
    </section>

    <section class="card card--front" aria-label="Card front">
      <div class="brand"><span class="brand-square"></span>Vantora Partners</div>
      <p class="person"><span class="person-name">Oliver Brantley</span> &nbsp;|&nbsp; Director</p>
      <p class="web">vantorapartners<span class="web-domain">.com.au</span></p>
    </section>
  </main>
</body>
</html>
```